Qorvane Management LLC Business Card

The sample logo was attached for the business Card Design for Traffic Control Company named Qorvane Management LLC. Card design needs to have the company logo and colors match the logo color. It will be nice to show some images of Traffic control signs or cones, even roads closer that math the company services

Target Market(s)

Temporary traffic control. Road closer.

Industry/Entity Type

Construction

Contact Information for Business Card

basic information, name, job title, address, email phone, website

Font styles to use
Serif
Sans Serif

Colors
F0912C
F2A743
F7CA91
FBE8D2
FDF5EE
EE7325
F08F49
F5BC92
FAE3D3
FDF4ED

```html
<!DOCTYPE html>
<html lang="en">
<head>
<meta charset="utf-8">
<title>Qorvane Management LLC – Business Card</title>
<link href="https://fonts.googleapis.com/css2?family=Montserrat:wght@600&family=Marcellus&display=swap" rel="stylesheet">
<style>
  :root {
    --charcoal: #444546;
    --charcoal-deep: #3a3b3c;
    --orange: #e96a2f;
    --white: #ffffff;
    --paper-light: #fbfbfb;
    --paper-shade: #e4e4e4;
    --text-grey: #4a4a4a;
    --stage: #2b2b2b;
  }
  * { box-sizing: border-box; margin: 0; padding: 0; }
  html, body {
    width: 1200px; height: 900px; overflow: hidden;
    background: var(--stage);
  }
  .stage {
    width: 1200px; height: 900px;
    display: flex; flex-direction: column; align-items: center; justify-content: center;
    gap: 40px;
  }
  .card {
    position: relative;
    width: 700px; height: 400px;
    overflow: hidden;
  }

  /* ---------- Front ---------- */
  .card-front { background: var(--charcoal); }
  .front-brand {
    position: absolute; left: 150px; top: 110px;
    display: flex; align-items: center; gap: 22px;
  }
  .brand-square {
    width: 58px; height: 58px; background: var(--orange);
  }
  .brand-name {
    font-family: "Montserrat", sans-serif; font-weight: 600;
    color: var(--white); letter-spacing: 4px; line-height: 1.25;
  }
  .front-brand .brand-name { font-size: 40px; }
  .front-brand .brand-name span { display: block; font-size: 26px; letter-spacing: 6px; }

  .front-band {
    position: absolute; left: 0; right: 0; top: 306px; height: 30px;
    background: linear-gradient(90deg, #dcdcdc 0%, var(--white) 45%, #e9e9e9 100%);
    clip-path: polygon(0 0, 150px 0, 150px 100%, 0 100%, 0 0, 225px 0, 100% 0, 100% 100%, 225px 100%);
  }
  .band-left  { position: absolute; top: 306px; height: 30px; left: 0; width: 150px; background: var(--white); clip-path: polygon(0 0, 100% 0, 88% 100%, 0 100%); }
  .band-right { position: absolute; top: 306px; height: 30px; left: 218px; right: 0; background: linear-gradient(90deg, var(--white) 0%, #f2f2f2 60%, #d9d9d9 100%); clip-path: polygon(4% 0, 100% 0, 100% 100%, 0 100%); }
  .slashes { position: absolute; }
  .front-slashes { left: 160px; top: 306px; }

  /* ---------- Back ---------- */
  .card-back {
    background: linear-gradient(110deg, var(--paper-shade) 0%, var(--paper-light) 45%, var(--white) 100%);
  }
  .back-brand {
    position: absolute; right: 48px; top: 44px;
    display: flex; align-items: center; gap: 16px;
  }
  .back-brand .brand-square { width: 40px; height: 40px; }
  .back-brand .brand-name { color: var(--charcoal); font-size: 28px; }
  .back-brand .brand-name span { display: block; font-size: 18px; letter-spacing: 5px; }

  .person { position: absolute; left: 44px; top: 150px; font-family: "Marcellus", serif; }
  .person-name { color: var(--orange); font-size: 30px; letter-spacing: 1px; }
  .person-title { color: var(--text-grey); font-size: 20px; margin-top: 2px; }

  .contact-list {
    position: absolute; left: 44px; top: 232px; list-style: none;
    font-family: "Marcellus", serif; font-size: 17px; color: var(--text-grey);
  }
  .contact-list li { display: flex; align-items: center; gap: 12px; height: 24px; }
  .contact-list svg { width: 15px; height: 15px; fill: var(--orange); flex: none; }

  .back-bar-main { position: absolute; left: 0; top: 344px; height: 20px; width: 594px; background: var(--charcoal); clip-path: polygon(0 0, 100% 0, 98% 100%, 0 100%); }
  .back-bar-end  { position: absolute; left: 636px; right: 0; top: 344px; height: 20px; background: var(--charcoal); clip-path: polygon(8% 0, 100% 0, 100% 100%, 0 100%); }
  .back-bar-base { position: absolute; left: 0; right: 0; top: 374px; height: 26px; background: var(--charcoal-deep); }
  .back-slashes { left: 596px; top: 340px; }
</style>
</head>
<body>
<main class="stage">

  <section class="card card-front" aria-label="Card front">
    <div class="front-brand">
      <div class="brand-square"></div>
      <div class="brand-name">QORVANE<span>MANAGEMENT LLC</span></div>
    </div>
    <div class="band-left"></div>
    <div class="band-right"></div>
    <svg class="slashes front-slashes" width="56" height="30" viewBox="0 0 56 30">
      <polygon points="14,0 26,0 16,30 4,30" fill="#e96a2f"/>
      <polygon points="32,0 44,0 34,30 22,30" fill="#e96a2f"/>
    </svg>
  </section>

  <section class="card card-back" aria-label="Card back">
    <div class="back-brand">
      <div class="brand-square"></div>
      <div class="brand-name">QORVANE<span>MANAGEMENT LLC</span></div>
    </div>

    <div class="person">
      <div class="person-name">EVAN ROURKE</div>
      <div class="person-title">Director</div>
    </div>

    <ul class="contact-list">
      <li>
        <svg viewBox="0 0 16 16"><path d="M1 5c2-3 12-3 14 0l-2 2-2-1V4H5v2L3 7zM4 8h8l2 6H2z"/></svg>
        (00) 0000 0000
      </li>
      <li>
        <svg viewBox="0 0 16 16"><circle cx="8" cy="8" r="7"/><path d="M3 6h4l1 3-2 3M10 3l1 3 3 1" stroke="#fff" stroke-width="1.2" fill="none"/></svg>
        www.qorvanemanagementllc.com
      </li>
      <li>
        <svg viewBox="0 0 16 16"><path d="M1 6l7-5 7 5v8H1z"/><path d="M1 6l7 5 7-5" stroke="#fff" stroke-width="1.2" fill="none"/></svg>
        evan@qorvanemanagementllc.com
      </li>
      <li>
        <svg viewBox="0 0 16 16"><path d="M8 0a5.5 5.5 0 0 1 5.5 5.5C13.5 10 8 16 8 16S2.5 10 2.5 5.5A5.5 5.5 0 0 1 8 0z"/><circle cx="8" cy="5.5" r="2.2" fill="#fff"/></svg>
        11 dummy city, dummy place, P.O Box 0000 Dummy Land
      </li>
    </ul>

    <div class="back-bar-main"></div>
    <svg class="slashes back-slashes" width="44" height="28" viewBox="0 0 44 28">
      <polygon points="10,0 20,0 12,28 2,28" fill="#e96a2f"/>
      <polygon points="26,0 36,0 28,28 18,28" fill="#e96a2f"/>
    </svg>
    <div class="back-bar-end"></div>
    <div class="back-bar-base"></div>
  </section>

</main>
</body>
</html>
```